Innovative biopolymers technology company needs a professional and engaging website

KELVO Polymer Systems AG is a biopolymer technology licensing company that enables plastic compounders to access new markets and innovate, plastic converters to manufacture bio-based, biodegradable, and bio-neutral plastic, and brand owners to satisfy the end-users’ demand for ‘greener’ plastics.

Our purpose is to help mankind ‘enjoy the convenience of plastic products guilt-free’. That’s why we’ve developed and patented our MARUSTEN® Technology, which enables producing plastics that are ‘kind at heart’. Our products are based on renewable materials, up to 99%, and can be – if required – 100% biodegradable at the same time.

Technically our bio plastics could replace 90% of today’s polyethylene applications. Therefore, our vision is ‘to make MARUSTEN® the world’s standard for the production and innovation in the area of biopolymers’.

We'd like to see website designs that portray us a serious technology company, whose products benefit the environment and brings alive our brand promise of 'kind at heart'.

Target Market(s)

Our primary target audience are plastics compounders that either want to produce resin/pellets, which allow their clients to produce either bio-based or biodegradable plastic.

Industry/Entity Type

Biodegradable

Requirements
Must have
• The website should be designed that it creates the desired user experience, represents the pre-defined structure, and meets our brand guidelines (see attached document KELVO_WebsiteDesignBrief_FinalVersion.pdf). Moreover, it needs to include the prepared content (see attached document KELVO_WebsiteContent_FinalVersion.doc).
Nice to have
• Ideally the selected Wordpress template should have an ordering functionality build-in already so that at a later stage we could order a product ordering process.
Should not have
• The design shouldn't look like purely an environmental company.

```html
<!DOCTYPE html>
<html lang="en">
<head>
<meta charset="utf-8">
<title>KELVO Polymer Systems AG</title>
<link href="https://fonts.googleapis.com/css2?family=Hind:wght@400;500;600;700&family=Arimo:wght@400;700&display=swap" rel="stylesheet">
<style>
:root{
  --ink:#111;
  --text:#555;
  --muted:#888;
  --teal:#1d6b7a;
  --line:#d8d8d8;
  --footer:#5b5b5b;
  --footer-text:#e6e6e6;
  --footer-link:#cfcfcf;
  --white:#fff;
  --sky:#2a9bd6;
}
*{box-sizing:border-box;margin:0;padding:0}
html,body{width:989px;height:1200px;overflow:hidden;background:var(--white)}
body{position:relative;font-family:"Arimo",Arial,sans-serif;color:var(--text)}
.abs{position:absolute}
a{color:var(--teal)}
.heading{font-family:"Hind",Arial,sans-serif}

/* header */
.brand{left:144px;top:16px;display:flex;align-items:center;gap:6px}
.brand-name{font-family:"Hind",sans-serif;font-weight:700;font-size:30px;color:var(--ink);line-height:1}
.brand-dot{width:12px;height:12px;border-radius:50%;background:var(--teal)}
.brand-tag{left:146px;top:48px;font-family:"Hind",sans-serif;font-size:11px;color:var(--ink)}
.search{left:528px;top:15px;width:159px;height:18px;border:1px solid #bbb;border-radius:9px;font-size:7.5px;color:#555;padding:4px 0 0 13px;letter-spacing:.2px}
.search svg{position:absolute;right:8px;top:3px}
.social{top:13px;display:flex;gap:7px}
.social span{width:20px;height:20px;border-radius:50%;background:var(--ink);display:block}
.lang{left:802px;top:15px;width:38px;height:16px;background:var(--ink);color:#fff;font-size:9px;padding:3px 0 0 8px}
.lang svg{position:absolute;right:7px;top:6px}
.nav{left:268px;top:49px;display:flex;gap:11px;font-family:"Hind",sans-serif;font-size:10.5px;color:var(--ink);letter-spacing:.1px}
.nav .active{border-bottom:2px solid var(--teal);padding-bottom:1px}

/* hero */
.hero{left:0;top:86px;width:989px;height:322px;background:linear-gradient(90deg,#9a9a9a 0%,#3c3c3c 18%,#2c2c2c 45%,#4a4a4a 62%,#d9d9d9 80%,#8e8e8e 100%)}
.hero-panel{left:142px;top:0;width:234px;height:322px;background:rgba(40,40,40,.55)}
.hero-title{left:166px;top:86px;font-family:"Hind",sans-serif;font-weight:700;font-size:23px;line-height:27px;color:#fff;letter-spacing:.5px}
.hero-sub{left:166px;top:198px;font-family:"Hind",sans-serif;font-size:20px;line-height:23px;color:#fff}
.hero-ctrl{top:10px;display:flex;gap:4px}
.hero-ctrl span{width:22px;height:22px;border:2px solid #fff;border-radius:50%;display:flex;align-items:center;justify-content:center}

/* features */
.card{top:433px;width:167px}
.card-img{height:88px;border:1px solid #ddd}
.card-title{font-family:"Hind",sans-serif;font-size:15.5px;line-height:17px;color:var(--ink);margin-top:12px}
.card-body{font-size:9.5px;line-height:12.5px;color:var(--text);margin-top:8px}
.divider{left:140px;top:666px;width:714px;height:14px;background:radial-gradient(ellipse at top,rgba(0,0,0,.12),rgba(0,0,0,0) 70%)}

/* latest thinking */
.section-title{font-family:"Hind",sans-serif;font-weight:700;font-size:21px;color:var(--ink);line-height:22px;letter-spacing:.3px}
.post{left:154px;width:446px;display:flex;gap:15px}
.post-thumb{width:74px;height:106px;border:1px solid #ccc;flex:none}
.post-title{font-family:"Hind",sans-serif;font-weight:600;font-size:14.5px;color:var(--ink);margin-top:4px}
.post-title span{color:var(--teal);font-weight:500}
.post-text{font-size:9.4px;line-height:11.5px;color:#666;margin-top:3px}
.post-time{font-size:9px;color:var(--teal);margin-top:6px}
.post-actions{display:flex;gap:10px;font-size:8px;color:#666;margin-top:14px}
.post-actions i{display:inline-block;width:7px;height:7px;background:#333;border-radius:1px;margin-right:3px;vertical-align:-1px}
.post-sep{left:241px;top:842px;width:360px;height:1px;background:var(--line)}
.vline{left:622px;top:690px;width:1px;height:326px;background:var(--line)}

/* posts column */
.chirp-badge{left:821px;top:689px;width:20px;height:20px;border-radius:50%;background:var(--sky)}
.chirp{left:644px;width:200px;display:flex;gap:12px}
.avatar{width:46px;height:46px;flex:none;border:1px solid #ddd}
.chirp-text{font-size:9.2px;line-height:11px;color:#9a9a9a;margin-top:2px}
.chirp-time{font-size:7.5px;color:#666;margin-top:4px}
.chirp-time i{display:inline-block;width:7px;height:6px;background:#333;margin-right:4px}
.chirp-label{left:640px;top:988px;font-family:"Hind",sans-serif;font-weight:700;font-size:12px;color:var(--sky)}
.join{left:731px;top:984px;width:108px;height:23px;border:1px solid #bbb;font-size:9px;font-weight:700;color:var(--ink);text-align:center;padding-top:6px}

/* footer */
.footer{left:0;top:1033px;width:989px;height:89px;background:var(--footer)}
.fcol{top:1046px}
.fcol h4{font-family:"Hind",sans-serif;font-weight:400;font-size:14px;color:var(--footer-text);line-height:16px}
.fcol p{font-size:8.5px;line-height:12.5px;color:var(--footer-link)}
.fcol h4+p{margin-top:4px}
.fcol .stack{line-height:19px}
.fsocial{left:757px;top:1087px;display:flex;gap:7px}
.fsocial span{width:20px;height:20px;border-radius:50%;background:var(--ink)}
.copy{left:157px;top:1136px;font-size:8.5px;line-height:14px;color:#333}
.copy span{color:var(--muted)}
.foot-brand{left:762px;top:1130px;display:flex;align-items:center;gap:4px}
.foot-brand b{font-family:"Hind",sans-serif;font-weight:700;font-size:22px;color:var(--ink);line-height:1}
.foot-tag{left:763px;top:1155px;font-family:"Hind",sans-serif;font-size:8.5px;color:var(--ink)}
</style>
</head>
<body>

<header>
  <div class="abs brand"><span class="brand-name">KELVO</span><span class="brand-dot"></span></div>
  <div class="abs brand-tag">kind at heart</div>
  <div class="abs search">ENTER KEYWORD
    <svg width="11" height="11" viewBox="0 0 11 11"><circle cx="4.5" cy="4.5" r="3.3" fill="none" stroke="#555" stroke-width="1.4"/><line x1="7" y1="7" x2="10" y2="10" stroke="#555" stroke-width="1.6"/></svg>
  </div>
  <div class="abs social" style="left:706px"><span></span><span></span><span></span></div>
  <div class="abs lang">EN<svg width="8" height="5" viewBox="0 0 8 5"><path d="M0 0h8L4 5z" fill="#fff"/></svg></div>
  <nav class="abs nav">
    <span class="active">HOME</span><span>BIO PLASTICS</span><span>MARUSTEN® TECHNOLOGY</span><span>LICENSE OPPORTUNITIES</span><span>LATEST THINKING</span><span>ABOUT US</span><span>CAREER</span><span>CONTACT US</span>
  </nav>
</header>

<section class="abs hero" role="img" aria-label="Hands holding young seedlings growing in newspaper pots labelled sustainable growth">
  <div class="abs hero-panel"></div>
  <h1 class="abs hero-title">THE MARKET FOR<br>BIO PLASTIC<br>GROWS EACH<br>YEAR BY 20%+.</h1>
  <p class="abs hero-sub">Ready to win this<br>market by storm?</p>
  <div class="abs hero-ctrl" style="left:764px">
    <span><svg width="8" height="10" viewBox="0 0 8 10"><path d="M6 1L2 5l4 4" fill="none" stroke="#fff" stroke-width="2"/></svg></span>
    <span><svg width="8" height="10" viewBox="0 0 8 10"><rect x="1" y="1" width="2" height="8" fill="#fff"/><rect x="5" y="1" width="2" height="8" fill="#fff"/></svg></span>
    <span><svg width="8" height="10" viewBox="0 0 8 10"><path d="M2 1l4 4-4 4" fill="none" stroke="#fff" stroke-width="2"/></svg></span>
  </div>
</section>

<section class="features">
  <article class="abs card" style="left:142px">
    <div class="card-img" role="img" aria-label="Corn cob wrapped around a plastic bottle" style="background:linear-gradient(135deg,#e4e4e4,#a9b887 55%,#d8d8d8)"></div>
    <h3 class="card-title">What type of bio plastic are you looking for? We have them all.</h3>
    <p class="card-body">Depending on what your requirements are, our bio plastic can either be <a>bio-based</a>, <a>biodegradable</a>, or <a>bio-neutral</a>.</p>
  </article>
  <article class="abs card" style="left:319px">
    <div class="card-img" role="img" aria-label="Green grass under a bright sky with carbon dioxide bubbles" style="background:linear-gradient(180deg,#e9f3f7 0%,#cfe7ee 40%,#7dbb3a 60%,#3f7f22 100%)"></div>
    <h3 class="card-title">MARUSTEN® Technology as the new industry standard</h3>
    <p class="card-body">Our bi-co-continuous process makes the production of bio plastics more economical and offers a platform for innovation.<br><a><u>Readmore.</u></a></p>
  </article>
  <article class="abs card" style="left:497px">
    <div class="card-img" role="img" aria-label="Chalk drawing of a head and a light bulb on a green board" style="background:linear-gradient(135deg,#2f6a45,#1f5234)"></div>
    <h3 class="card-title">Ready to get started? We have two types of licenses on offer.</h3>
    <p class="card-body">To help you access new markets or innovate in biopolymers we offer two licenses:<br><a><u>Compounding License</u></a> or <a><u>Technology License</u></a>.</p>
  </article>
  <article class="abs card" style="left:676px">
    <div class="card-img" role="img" aria-label="Two scientists in a lab holding a flask of green liquid" style="background:linear-gradient(90deg,#2c6fa8,#e9eef2 45%,#4aa6d8)"></div>
    <h3 class="card-title">We’re looking for you, Join us Today.</h3>
    <p class="card-body">As a growing company we’re looking for talented colleagues Check-out what <a><u>Life at KELVO</u></a> is like or when ready <a><u>join us</u></a>.</p>
  </article>
</section>

<div class="abs divider"></div>

<section class="latest">
  <h2 class="abs section-title" style="left:148px;top:694px">LATEST THINKING</h2>
  <article class="abs post" style="top:728px">
    <div class="post-thumb" role="img" aria-label="Report cover on bioplastics demand with a field of plants" style="background:linear-gradient(180deg,#7a6a4a,#3f5a30)"></div>
    <div>
      <h3 class="post-title">Reviewed.... <span>Riverside Flats for Sale Rent</span></h3>
      <p class="post-text">Lorem ipsum dolor sit amet, consectetuer adipiscing elit, sed diam nonummy nibh euismod tincidunt ut laoreet dolore magna aliquam erat volutpat. Ut wisi enim ad minim veniam, quis nostrud exerci tation ullamcorper suscipit lobortis nisl ut aliquip ex ea commodo consequat....</p>
      <p class="post-time">12 minutes ago</p>
      <div class="post-actions"><span><i></i>Like</span><span><i></i>Share</span><span><i></i>Comment</span><span><i></i>Post</span></div>
    </div>
  </article>
  <div class="abs post-sep"></div>
  <article class="abs post" style="top:850px">
    <div class="post-thumb" role="img" aria-label="Fresh produce in a clear bioplastic package" style="background:linear-gradient(180deg,#eef0ec,#a9d36a 60%,#e6e6e6)"></div>
    <div>
      <h3 class="post-title">Reviewed.... <span>Riverside Flats for Sale Rent</span></h3>
      <p class="post-text">Lorem ipsum dolor sit amet, consectetuer adipiscing elit, sed diam nonummy nibh euismod tincidunt ut laoreet dolore magna aliquam erat volutpat. Ut wisi enim ad minim veniam, quis nostrud exerci tation ullamcorper suscipit lobortis nisl ut aliquip ex ea commodo consequat....</p>
      <p class="post-time">12 minutes ago</p>
      <div class="post-actions"><span><i></i>Like</span><span><i></i>Share</span><span><i></i>Comment</span><span><i></i>Post</span></div>
    </div>
  </article>
</section>

<div class="abs vline"></div>

<aside class="posts">
  <h2 class="abs section-title" style="left:647px;top:692px">WHAT WE’RE<br>POSTING ABOUT</h2>
  <div class="abs chirp-badge"></div>
  <div class="abs" style="left:644px;top:740px;width:180px;height:1px;background:var(--line)"></div>
  <div class="abs chirp" style="top:758px">
    <div class="avatar" role="img" aria-label="Profile photo of a team member" style="background:#c9a58a"></div>
    <div><p class="chirp-text">Lorem ipsum dolor sit amet, consectetuer adipiscing elit, sed diam nonummy nibh euismod tincidunt</p><p class="chirp-time"><i></i>2 hours Ago</p></div>
  </div>
  <div class="abs chirp" style="top:834px">
    <div class="avatar" role="img" aria-label="Profile photo of a team member" style="background:#b98a6e"></div>
    <div><p class="chirp-text">Laoreet dolore magna aliquam erat volutpat. Ut wisi enim ad minim veniam, quis nostrud</p><p class="chirp-time"><i></i>2 hours Ago</p></div>
  </div>
  <div class="abs chirp" style="top:909px">
    <div class="avatar" role="img" aria-label="Profile photo of a team member" style="background:#8e8a88"></div>
    <div><p class="chirp-text">Exerci tation ullamcorper suscipit lobortis nisl ut aliquip ex ea commodo consequat....</p><p class="chirp-time"><i></i>2 hours Ago</p></div>
  </div>
  <div class="abs chirp-label">Chirper</div>
  <div class="abs join">Join the conversation</div>
</aside>

<footer>
  <div class="abs footer"></div>
  <div class="abs fcol" style="left:157px"><h4>Bio Plastics</h4><p>MARUSTEN® Bio-based<br>MARUSTEN® Biodegradable<br>MARUSTEN® Bio-neutral</p></div>
  <div class="abs fcol" style="left:292px"><h4>MARUSTEN® Technology</h4><p>What makes it different<br>How it works<br>FAQ</p></div>
  <div class="abs fcol" style="left:454px"><h4>License opportunities</h4><p>Become a licensed compounder<br>Become a technology licensee</p></div>
  <div class="abs fcol" style="left:629px"><h4 class="stack">Latest thinking<br>About us<br>Career</h4></div>
  <div class="abs fcol" style="left:757px"><h4 class="stack">Contact Us<br><span style="color:var(--footer-link)">Connect with Us</span></h4></div>
  <div class="abs fsocial"><span></span><span></span><span></span></div>
  <p class="abs copy">© 2013 KELVO Polymer Systems AG. All rights reserved. MARUSTEN® and VELARIN® are both registered<br><span>trademarks and owned by KELVO Polymer Systems AG.</span></p>
  <div class="abs foot-brand"><b>KELVO</b><span class="brand-dot" style="width:9px;height:9px"></span></div>
  <div class="abs foot-tag">kind at heart</div>
</footer>

</body>
</html>
```